Update the A4 Specials Page for Restaurant/Cafe

Provide a MINIMALIST attractive Specials page we can print weekly for our food and drink specials to give to our guests. Final design is to be provided in WORD Document so it can be easily edited by Manager. Should be black text and MINIMALIST to minimise ink usage as we print hundreds a week. We have UPLOADED the existing page as a template for you to update. Maybe logo can stay, see what you think. Or delete it and do something else. Keep it simple. Choose a good FONT. Could be a little playful with a cocktail ICON or something. Our existing menus can be seen at www.tallpinebistro.com.au and they are using font Alegreya. Please note we are unable to provide any feedback to designers, however we really do appreciate your time if you are submitting a design. Thank you for your participation.

```html
<!DOCTYPE html>
<html lang="en">
<head>
<meta charset="utf-8">
<title>Tall Pine Bistro – Weekly Specials</title>
<link rel="stylesheet" href="https://fonts.googleapis.com/css2?family=Alegreya+Sans:wght@700;800&family=Roboto:wght@400;700&display=swap">
<style>
  :root {
    --rust: #b5532a;
    --navy: #1d3b73;
    --ink: #111111;
    --paper: #ffffff;
    --backdrop: #f2f2f2;
  }
  * { margin: 0; padding: 0; box-sizing: border-box; }
  html, body { width: 1200px; height: 1000px; overflow: hidden; }
  body { background: var(--backdrop); position: relative; font-family: "Roboto", Arial, sans-serif; color: var(--ink); }

  .page { position: absolute; left: 298px; top: 75px; width: 590px; height: 835px; background: var(--paper); }
  .page-frame { position: absolute; left: 0; top: 0; width: 1200px; height: 1000px; pointer-events: none; }

  .header-name, .header-title {
    position: absolute; top: 143px; height: 84px;
    border: 2px solid var(--rust);
    display: flex; align-items: center; justify-content: center; text-align: center;
    font-family: "Alegreya Sans", Arial, sans-serif; font-weight: 700; color: var(--navy);
  }
  .header-name { left: 365px; width: 181px; font-size: 26px; line-height: 1.0; letter-spacing: 0.5px; }
  .header-title { left: 545px; width: 279px; font-size: 23px; line-height: 1.1; border-left: none; }

  .icon-tile {
    position: absolute; left: 377px; width: 97px; height: 111px;
    border: 2px solid var(--rust); border-radius: 10px;
    display: flex; align-items: center; justify-content: center;
  }
  .icon-tile svg { width: 80px; height: 80px; fill: none; stroke: var(--rust); stroke-width: 2; stroke-linecap: round; stroke-linejoin: round; }

  .dish-name { position: absolute; left: 493px; font-family: "Alegreya Sans", Arial, sans-serif; font-weight: 700; font-size: 20px; line-height: 25px; letter-spacing: 0.3px; }
  .dish-notes { position: absolute; left: 493px; font-size: 15px; line-height: 19px; letter-spacing: 0.2px; }
  .price-tag {
    position: absolute; left: 747px; width: 73px; height: 34px;
    border: 1.5px solid var(--ink); border-radius: 8px;
    display: flex; align-items: center; justify-content: center;
    font-weight: 700; font-size: 15px;
  }
  .section-label { position: absolute; font-family: "Alegreya Sans", Arial, sans-serif; font-weight: 700; font-size: 14.5px; }
</style>
</head>
<body>
  <div class="page"></div>

  <svg class="page-frame" viewBox="0 0 1200 1000" aria-hidden="true">
    <g fill="#b5532a">
      <rect x="327" y="103" width="20" height="20"/>
      <rect x="839" y="103" width="20" height="20"/>
      <rect x="327" y="861" width="20" height="20"/>
      <rect x="839" y="861" width="20" height="20"/>
    </g>
    <g stroke="#b5532a" stroke-width="1.5">
      <line x1="362" y1="103" x2="548" y2="103"/>
      <line x1="637" y1="103" x2="823" y2="103"/>
      <line x1="410" y1="111" x2="776" y2="111"/>
      <line x1="410" y1="873" x2="776" y2="873"/>
      <line x1="362" y1="881" x2="548" y2="881"/>
      <line x1="637" y1="881" x2="823" y2="881"/>
      <line x1="327" y1="140" x2="327" y2="520"/>
      <line x1="327" y1="560" x2="327" y2="845"/>
      <line x1="335" y1="212" x2="335" y2="505"/>
      <line x1="335" y1="620" x2="335" y2="790"/>
      <line x1="858" y1="140" x2="858" y2="520"/>
      <line x1="858" y1="560" x2="858" y2="845"/>
      <line x1="850" y1="212" x2="850" y2="505"/>
      <line x1="850" y1="620" x2="850" y2="790"/>
    </g>
  </svg>

  <div class="header-name">TALL PINE<br>BISTRO</div>
  <div class="header-title">WEEKLY<br>SPECIALS</div>

  <div class="icon-tile" style="top:260px">
    <svg viewBox="0 0 80 80"><path d="M14 52 A26 26 0 0 1 66 52 Z"/><circle cx="40" cy="23" r="3"/><rect x="8" y="53" width="64" height="5" rx="2.5"/><path d="M24 44 A18 18 0 0 1 30 34"/></svg>
  </div>
  <div class="dish-name" style="top:278px">CHICKEN FILO</div>
  <div class="dish-notes" style="top:316px">Creamy Chicken with Pinenuts, wrapped in Filo<br>Pastry. Served with Side Salad &amp; Zulu Sauce.</div>
  <div class="price-tag" style="top:260px">$24</div>

  <div class="icon-tile" style="top:400px">
    <svg viewBox="0 0 80 80"><path d="M34 12 q-4 4 0 8 q4 4 0 8"/><path d="M40 10 q-4 4 0 8 q4 4 0 8"/><path d="M46 12 q-4 4 0 8 q4 4 0 8"/><path d="M12 36 h56 q-3 20 -18 24 h-20 q-15 -4 -18 -24 z"/><path d="M50 42 q-2 8 -8 12"/><rect x="12" y="66" width="56" height="4" rx="2"/></svg>
  </div>
  <div class="dish-name" style="top:413px">MINESTRONE SOUP</div>
  <div class="dish-notes" style="top:451px">Served with Garlic Bread.</div>
  <div class="price-tag" style="top:400px">$8</div>

  <div class="section-label" style="left:366px;top:538px">COCKTAIL SPECIAL</div>
  <div class="icon-tile" style="top:563px">
    <svg viewBox="0 0 80 80"><path d="M12 22 h48 l-24 28 z"/><line x1="18" y1="29" x2="54" y2="29"/><line x1="36" y1="50" x2="36" y2="70"/><line x1="26" y1="72" x2="46" y2="72"/><line x1="10" y1="10" x2="38" y2="42"/><circle cx="60" cy="18" r="7"/></svg>
  </div>
  <div class="dish-name" style="top:575px">PASSIONISTA</div>
  <div class="dish-notes" style="top:613px">Vodka, Passionfruit Pulp, Mango Puree<br>Top up with Ginger &amp; Lemon Kombucha.</div>
  <div class="price-tag" style="top:563px">$17</div>

  <div class="section-label" style="left:358px;top:698px">CRAFT BEER SPECIAL</div>
  <div class="icon-tile" style="top:724px">
    <svg viewBox="0 0 80 80"><path d="M20 22 q-4 -8 4 -10 q4 -6 12 -3 q6 -4 12 1 q8 0 6 8 q2 4 -2 6 h-32 z"/><rect x="22" y="24" width="30" height="48" rx="3"/><path d="M52 34 h6 q6 0 6 6 v10 q0 6 -6 6 h-6"/><line x1="30" y1="32" x2="30" y2="64"/><line x1="37" y1="32" x2="37" y2="64"/><line x1="44" y1="32" x2="44" y2="64"/></svg>
  </div>
  <div class="dish-name" style="top:728px">COPPER KETTLE<br>MANGO CLOUD</div>
  <div class="dish-notes" style="top:791px">Tropical Pale Ale - 4.8% Alc.</div>
  <div class="price-tag" style="top:724px">$10</div>
</body>
</html>
```